Online video and marketing company business cards

Need to get some new business cards designed to fit with our new logo. The cards should be professional, clean and simple.

Cards should have:

Name
Position
2 line address
telephone
mobile
email address
web address

We need to have our logo and if possible say what we do...
ONLINE FILM PRODUCTION & STRATEGY

Industry/Entity Type

Marketing

```html
<!DOCTYPE html>
<html lang="en">
<head>
<meta charset="utf-8">
<title>Vistareel Business Cards</title>
<link href="https://fonts.googleapis.com/css2?family=Questrial&family=Montserrat:wght@600&display=swap" rel="stylesheet">
<style>
  :root {
    --stage: #e8ebee;
    --card-white: #fbfbfa;
    --navy: #1f3a5c;
    --teal: #3d93b3;
    --blue-deep: #173f63;
    --blue-mid: #2a6589;
    --tagline: #c9dbe6;
    --divider: #e2e4e6;
  }
  * { margin: 0; padding: 0; box-sizing: border-box; }
  html, body { width: 1200px; height: 800px; overflow: hidden; }
  body {
    background: var(--stage);
    font-family: "Questrial", "Century Gothic", sans-serif;
    position: relative;
  }
  .card {
    position: absolute;
    top: 257px;
    width: 500px;
    height: 286px;
    border-radius: 3px;
    box-shadow: 0 10px 28px rgba(20, 40, 60, 0.18);
    overflow: hidden;
  }
  .card-front { left: 80px; background: var(--card-white); }
  .card-back {
    left: 620px;
    background: linear-gradient(135deg, var(--blue-deep) 0%, var(--blue-mid) 100%);
  }

  .brand {
    display: flex;
    align-items: center;
    gap: 10px;
    font-size: 40px;
    line-height: 1;
    letter-spacing: -0.5px;
  }
  .brand-dot {
    width: 30px; height: 30px;
    border-radius: 50%;
    flex: none;
  }
  .card-front .brand { position: absolute; left: 34px; top: 120px; color: var(--teal); }
  .card-front .brand-dot { background: var(--navy); }

  .front-divider {
    position: absolute;
    left: 292px; top: 0; bottom: 0;
    width: 1px;
    background: var(--divider);
  }
  .contact { position: absolute; left: 314px; top: 34px; color: var(--navy); }
  .contact-name {
    font-family: "Montserrat", "Century Gothic", sans-serif;
    font-weight: 600;
    font-size: 17px;
    color: var(--teal);
    letter-spacing: 0.5px;
  }
  .contact-role { font-size: 14px; margin-top: 1px; }
  .contact-list { list-style: none; margin-top: 22px; }
  .contact-list li {
    display: flex; align-items: center; gap: 9px;
    font-size: 12.5px; height: 19px;
  }
  .contact-list svg { width: 13px; height: 13px; flex: none; }
  .address { font-size: 13px; line-height: 19px; margin-top: 22px; margin-left: 22px; }

  .card-back .brand { position: absolute; left: 44px; top: 188px; color: var(--teal); }
  .card-back .brand-dot { background: #ffffff; }
  .tagline {
    position: absolute; left: 300px; top: 180px;
    color: var(--tagline);
    font-size: 16px; line-height: 21px;
  }
  .tagline span { display: block; padding-left: 26px; }
</style>
</head>
<body>
  <section class="card card-front" aria-label="Business card front">
    <div class="brand"><span class="brand-dot"></span>vistareel</div>
    <div class="front-divider"></div>
    <div class="contact">
      <p class="contact-name">SAM PORTER</p>
      <p class="contact-role">Manager</p>
      <ul class="contact-list">
        <li>
          <svg viewBox="0 0 14 14" fill="none" stroke="#3d93b3" stroke-width="1.1"><circle cx="7" cy="7" r="6.3"/><rect x="4.8" y="3.4" width="4.4" height="7.2" rx="0.8"/></svg>
          +44(0)207 555 0142
        </li>
        <li>
          <svg viewBox="0 0 14 14" fill="none" stroke="#3d93b3" stroke-width="1.1"><circle cx="7" cy="7" r="6.3"/><path d="M4.6 4c.4 2.6 2.4 4.8 5.2 5.4l.6-1.2-1.4-.8-.6.6c-.9-.5-1.6-1.2-2-2.1l.6-.6-.8-1.4z"/></svg>
          +44(0)203 555 0178
        </li>
        <li>
          <svg viewBox="0 0 14 14" fill="none" stroke="#3d93b3" stroke-width="1.1"><circle cx="7" cy="7" r="6.3"/><rect x="3.8" y="4.8" width="6.4" height="4.4"/><path d="M3.8 4.8 7 7.4l3.2-2.6"/></svg>
          info@vistareel.com
        </li>
        <li>
          <svg viewBox="0 0 14 14" fill="none" stroke="#3d93b3" stroke-width="1.1"><circle cx="7" cy="7" r="6.3"/><ellipse cx="7" cy="7" rx="2.6" ry="6.3"/><path d="M0.7 7h12.6M1.8 4h10.4M1.8 10h10.4"/></svg>
          www.vistareel.com
        </li>
      </ul>
      <p class="address">14, Marlow Grove<br>London N4 2QT U.K.</p>
    </div>
  </section>

  <section class="card card-back" aria-label="Business card back">
    <div class="brand"><span class="brand-dot"></span>vistareel</div>
    <p class="tagline">Online Film Production<span>&amp; Strategy</span></p>
  </section>
</body>
</html>
```